Real Estate Email Signature

I need a professional looking real estate email signature with my picture, logo, and Name, Real Estate Broker/Realtor, and Top of Quorvane logo

```html
<!DOCTYPE html>
<html lang="en">
<head>
<meta charset="utf-8">
<title>Jon Vesk – Email Signature</title>
<link rel="stylesheet" href="https://fonts.googleapis.com/css2?family=Montserrat:wght@500;600;700;800&display=swap">
<style>
  :root {
    --navy: #0c5580;
    --navy-deep: #0a3f63;
    --badge: #22306f;
    --white: #ffffff;
    --sky-soft: #d6e9f8;
    --sky-pale: #eef6fc;
    --edge: #eef1f4;
    --page: #ffffff;
  }
  * { margin: 0; padding: 0; box-sizing: border-box; }
  html, body {
    width: 1200px;
    height: 1117px;
    overflow: hidden;
    background: var(--page);
    font-family: "Montserrat", Arial, sans-serif;
  }
  .signature {
    position: absolute;
    left: 240px;
    top: 170px;
    width: 720px;
    height: 167px;
    background: var(--white);
    overflow: hidden;
    border: 1px solid var(--edge);
  }
  .signature__texture {
    position: absolute;
    left: 0;
    top: 0;
    width: 205px;
    height: 107px;
    background: linear-gradient(90deg, var(--sky-soft) 0%, var(--sky-pale) 70%, var(--white) 100%);
  }
  .signature__band {
    position: absolute;
    left: 0;
    top: 107px;
    width: 100%;
    height: 60px;
    background: var(--navy);
  }
  .signature__photo {
    position: absolute;
    left: 40px;
    top: 20px;
    width: 112px;
    height: 112px;
    border-radius: 50%;
    border: 5px solid var(--navy-deep);
    background: linear-gradient(180deg, #b08a76 0%, #8c7668 55%, #7d8893 100%);
  }
  .signature__name {
    position: absolute;
    left: 198px;
    top: 69px;
    font-size: 50px;
    font-weight: 800;
    line-height: 1;
    letter-spacing: 1px;
    white-space: nowrap;
    background: linear-gradient(to bottom, var(--navy) 0, var(--navy) 38px, var(--white) 38px, var(--white) 100%);
    -webkit-background-clip: text;
    background-clip: text;
    color: transparent;
  }
  .signature__title {
    position: absolute;
    left: 200px;
    top: 134px;
    font-size: 16px;
    font-weight: 500;
    color: var(--white);
    letter-spacing: 0.4px;
    white-space: nowrap;
  }
  .brand {
    position: absolute;
    left: 533px;
    top: 0;
    width: 160px;
    text-align: center;
  }
  .brand__mark {
    width: 62px;
    height: 62px;
    margin: 6px auto 0;
    border-radius: 50%;
    background: var(--navy);
  }
  .brand__name {
    margin-top: 6px;
    font-size: 16px;
    font-weight: 700;
    color: var(--navy);
    letter-spacing: 0.2px;
    line-height: 1;
    white-space: nowrap;
  }
  .brand__tagline {
    margin-top: 2px;
    font-size: 7px;
    font-weight: 700;
    color: var(--navy);
    letter-spacing: 1px;
    white-space: nowrap;
  }
  .award {
    position: absolute;
    left: 544px;
    top: 121px;
    width: 150px;
    height: 37px;
    background: var(--badge);
    color: var(--white);
    font-size: 12px;
    font-weight: 700;
    letter-spacing: 0.5px;
    white-space: nowrap;
    display: flex;
    align-items: center;
    justify-content: center;
    box-shadow: 0 2px 3px rgba(0,0,0,0.3);
  }
</style>
</head>
<body>
  <section class="signature">
    <div class="signature__texture" role="img" aria-label="Light blue halftone texture"></div>
    <div class="signature__band"></div>
    <div class="signature__photo" role="img" aria-label="Portrait photo of Jon Vesk"></div>
    <h1 class="signature__name">JON VESK</h1>
    <p class="signature__title">Real Estate Broker/Realtor</p>
    <div class="brand">
      <div class="brand__mark"></div>
      <p class="brand__name">VESK PROPERTIES</p>
      <p class="brand__tagline">REAL ESTATE SERVICES</p>
    </div>
    <div class="award">TOP OF QUORVANE</div>
  </section>
</body>
</html>
```